Design cd cover for the vocal group: Ember, cd title Harbor Light. Cd cover is for EP release to be followed by full album. Songs are: Sizwe Langa Khona(Lift high the lamp); Cold River Road; Ngolwazi(Guide me through the night); When Rain Falls. There is no track entitled harbor light; the concept of the sound of gospel music as embodied in the music tracks - contemporary and traditional - is the basis of the album title.
NB: Project can close Tuesday 12 November to account for the 5 days as I do not count Saturday as a working day.
Hey guys,
Hello to everyone. I would like to take this opportunity to say thank you for your participation. Your submissions have been great and much appreciated. Forgive me for not being able to provide feedback to all of you. The time has come for me to make selection decisions and I would like to say thank you to all for your participation, you have been great and amazing.

```html
<!DOCTYPE html>
<html lang="en">
<head>
<meta charset="utf-8">
<title>Harbor Light — Ember EP Cover</title>
<link rel="stylesheet" href="https://fonts.googleapis.com/css2?family=Exo+2:wght@800;900&family=Oswald:wght@500&display=swap">
<style>
  :root {
    --sky-deep: #1d3944;
    --sky-teal: #3d6670;
    --sky-haze: #cfd0bf;
    --sun-glow: #f7f1de;
    --horizon: #b9b29c;
    --field-gold: #9a8456;
    --field-dark: #3a3326;
    --road-dark: #221e19;
    --ink-white: #ffffff;
    --rule: rgba(40, 40, 40, 0.55);
    --track-ink: #1e1e1e;
  }
  * { margin: 0; padding: 0; box-sizing: border-box; }
  html, body {
    width: 1200px; height: 576px; overflow: hidden; background: #ffffff;
  }
  .spread { position: relative; width: 1200px; height: 576px; display: flex; }
  .panel { position: relative; width: 600px; height: 576px; overflow: hidden; }
  .landscape {
    position: absolute; inset: 0;
    background:
      radial-gradient(ellipse 340px 200px at 50% 300px, var(--sun-glow) 0%, rgba(247,241,222,0.6) 45%, rgba(247,241,222,0) 100%),
      linear-gradient(to bottom,
        var(--sky-deep) 0px,
        var(--sky-teal) 70px,
        var(--sky-haze) 200px,
        var(--sun-glow) 300px,
        var(--horizon) 340px,
        var(--field-gold) 380px,
        #6e5c3c 450px,
        var(--field-dark) 520px,
        var(--road-dark) 576px);
  }
  .title-block { position: absolute; color: var(--ink-white); font-family: "Exo 2", sans-serif; font-weight: 900; line-height: 1; }
  .title-main { display: block; text-transform: uppercase; letter-spacing: -2px; transform-origin: center top; }
  .title-sub { display: block; text-align: right; text-transform: uppercase; font-weight: 800; }

  .front .title-block { left: 40px; top: 62px; width: 515px; }
  .front .title-main { font-size: 124px; text-align: center; transform: scaleY(1.12); }
  .front .title-sub { font-size: 42px; margin-top: 8px; }

  .group-name {
    position: absolute; right: 50px; top: 504px;
    color: var(--ink-white); font-family: "Exo 2", sans-serif; font-weight: 800;
    font-size: 22px; letter-spacing: 2px; text-transform: uppercase;
  }

  .back .title-block { left: 195px; top: 96px; width: 210px; }
  .back .title-main { font-size: 52px; text-align: center; letter-spacing: -1px; }
  .back .title-sub { font-size: 17px; margin-top: -2px; }

  .tracklist {
    position: absolute; left: 220px; top: 178px; width: 160px;
    list-style: none; text-align: center; color: var(--track-ink);
    font-family: "Oswald", sans-serif; font-weight: 500; text-transform: uppercase;
  }
  .track { padding: 3px 0 4px; border-bottom: 1px dotted var(--rule); }
  .track:last-child { border-bottom: none; }
  .track-title { display: block; font-size: 15px; line-height: 1.2; letter-spacing: 0.3px; }
  .track-translation { display: block; font-size: 11px; line-height: 1.2; font-style: italic; letter-spacing: 0.3px; }
</style>
</head>
<body>
<main class="spread">
  <section class="panel front">
    <div class="landscape" role="img" aria-label="Photograph of a figure walking down a dirt road through golden fields toward a bright hazy horizon under a teal sky"></div>
    <h1 class="title-block">
      <span class="title-main">Harbor</span>
      <span class="title-sub">Light</span>
    </h1>
    <p class="group-name">Ember</p>
  </section>

  <section class="panel back">
    <div class="landscape" role="img" aria-label="Photograph of an empty dirt road through golden fields toward a bright hazy horizon under a teal sky"></div>
    <h2 class="title-block">
      <span class="title-main">Harbor</span>
      <span class="title-sub">Light</span>
    </h2>
    <ol class="tracklist">
      <li class="track">
        <span class="track-title">Sizwe Langa Khona</span>
        <span class="track-translation">(Lift high the lamp)</span>
      </li>
      <li class="track"><span class="track-title">Cold River Road</span></li>
      <li class="track">
        <span class="track-title">Ngolwazi</span>
        <span class="track-translation">(Guide me through the night)</span>
      </li>
      <li class="track"><span class="track-title">When Rain Falls</span></li>
    </ol>
  </section>
</main>
</body>
</html>
```